Design new Brackwater Asset business card 2016

We need a new business card for our company Brackwater Asset Partners. We are a niche Alternative Investment Fund Manager based in Chester, in the North West of the UK.We market our services to global institutions such as banks, insurance companies, pension funds, etc. as well as wealthy individuals. Our main markets are Europe (Germany\France\Switzerland), the US and parts of Asia.
The design needs to be in line with existing company branding. Life the assets we deal with, the business card might suggest, "niche\alternative" type of attributes - however, it needs to remain professional, clean and appropriate for our client base.
Our existing business card format with relevant factual information is included, along with logo and branding details.

Target Market(s)

We market our services to global institutions such as banks, insurance companies, pension funds, etc. as well as wealthy individuals.

Industry/Entity Type

Financial Service

Contact Information for Business Card

please see attached pdf for information on existing business card which we should aim to convey on your new design. However:
- the wording "Brackwater Asset Partners Ltd is Authorised and Regulated
by the Monetary Oversight Bureau. Registered No. 7139046" should be replaced with , "Brackwater Asset Partners Ltd is an Alternative Investment Fund Manager Authorised and Regulated by the Monetary Oversight Bureau. Registered No. 7139046"
- the "reception" word on reverse can be omitted.
- the "retail: www.toplivanex.co.uk" wording can be omitted.
- the QR code is not required in the new version.

Font styles to use
Serif
Sans Serif

Requirements
Must have
• information on current business card, subject to comments provided above.
Nice to have
• Use of areas of solid colour instead of large areas of white space might be nice to experiment with. However, still need to have the general look and feel of the brand as presented on our website www.bwfundco.co.uk
• If we had space for 3 bullet points describing what we do\who we are, this might be good to try out. e.g. alternative investment fund manager, longevity specialist, founded 1990.
• Also, we have a new tag line, "expertise with longevity" which might fit nicely somewhere on the business card.
Should not have
• - no QR code
• - should not use all the colours in our logo as it looks very garish! Using one or two colours with black\white etc, seems to work better.

```html
<!DOCTYPE html>
<html lang="en">
<head>
<meta charset="utf-8">
<title>Brackwater Asset Partners – Business Card</title>
<link rel="stylesheet" href="https://fonts.googleapis.com/css2?family=Tinos&family=Arimo&display=swap">
<style>
  :root {
    --card-light: #ffffff;
    --card-mid: #e6e6e6;
    --card-edge: #cfcfcf;
    --sweep: #efefef;
    --ink-brown: #4a2612;
    --ink-black: #111111;
    --brand-mark: #c8372d;
  }
  html, body {
    margin: 0;
    padding: 0;
    width: 1200px;
    height: 741px;
    overflow: hidden;
    background: var(--card-mid);
  }
  .card {
    position: relative;
    width: 1200px;
    height: 741px;
    overflow: hidden;
    background: radial-gradient(ellipse 620px 460px at 420px 280px, var(--card-light) 0%, var(--card-mid) 60%, var(--card-edge) 100%);
  }
  .card__sweep {
    position: absolute;
    inset: 0;
  }
  .brand {
    position: absolute;
    top: 40px;
    right: 40px;
    display: flex;
    align-items: center;
    gap: 16px;
  }
  .brand__dot {
    width: 46px;
    height: 46px;
    border-radius: 50%;
    background: var(--brand-mark);
  }
  .brand__name {
    font-family: "Tinos", "Times New Roman", serif;
    font-size: 26px;
    color: var(--ink-brown);
  }
  .person {
    position: absolute;
    left: 460px;
    top: 330px;
    width: 340px;
    text-align: center;
  }
  .person__name {
    margin: 0;
    font-family: "Tinos", "Times New Roman", serif;
    font-weight: 400;
    font-size: 56px;
    line-height: 1;
    color: var(--ink-brown);
  }
  .person__role {
    margin: 18px 0 0;
    font-family: "Tinos", "Times New Roman", serif;
    font-size: 23px;
    color: var(--ink-black);
  }
  .contact {
    position: absolute;
    right: 43px;
    top: 562px;
    margin: 0;
    padding: 0;
    list-style: none;
    text-align: right;
  }
  .contact__item {
    font-family: "Arimo", Arial, sans-serif;
    font-size: 23px;
    line-height: 35.5px;
    color: var(--ink-black);
  }
  .contact__label {
    font-family: "Tinos", "Times New Roman", serif;
    color: var(--ink-brown);
    margin-right: 6px;
  }
</style>
</head>
<body>
  <main class="card">
    <svg class="card__sweep" width="1200" height="741" viewBox="0 0 1200 741" aria-hidden="true">
      <path d="M0 560 C 260 420, 520 520, 760 660 C 900 720, 1080 560, 1200 390 L 1200 741 L 0 741 Z" fill="var(--sweep)" opacity="0.85"/>
      <path d="M0 560 C 260 420, 520 520, 760 660 C 900 720, 1080 560, 1200 390" fill="none" stroke="var(--card-edge)" stroke-width="3"/>
    </svg>

    <div class="brand">
      <span class="brand__name">Brackwater Asset Partners</span>
      <span class="brand__dot"></span>
    </div>

    <section class="person">
      <h1 class="person__name">Martin Hale</h1>
      <p class="person__role">Non-Executive Chairman</p>
    </section>

    <ul class="contact">
      <li class="contact__item"><span class="contact__label">T:</span>+ 44 (0) 1244 560281</li>
      <li class="contact__item"><span class="contact__label">M:</span> +44 (0)7700 914362</li>
      <li class="contact__item"><span class="contact__label">E:</span>mhale@bwfundco.co.uk</li>
    </ul>
  </main>
</body>
</html>
```